Yard sign

I want it to look similar to this one,

change name to DRAVEK and submit new ideas

Also would like to improvise a bit. let's not make exactly the same thing

would like to change to: Connecticut #1 Company

also change phone to 203-555-0147
and website to
dravekllc.com

this is yard sign. size is 24' Width and 32' Height

Target Market(s)

Roof

Industry/Entity Type

Roofing

Requirements
Must have
• similar colors or add something new

```html
<!DOCTYPE html>
<html lang="en">
<head>
<meta charset="utf-8">
<title>DRAVEK Roofing Yard Sign</title>
<link rel="stylesheet" href="https://fonts.googleapis.com/css2?family=Montserrat:wght@300;500;800;900&display=swap">
<style>
  :root {
    --sign-yellow: #fdcd00;
    --sign-red: #fb0000;
    --sign-black: #000000;
    --sign-white: #ffffff;
    --page-bg: #fefefe;
  }
  html, body {
    margin: 0;
    padding: 0;
    width: 1200px;
    height: 1000px;
    overflow: hidden;
    background: var(--page-bg);
  }
  .yard-sign {
    position: absolute;
    left: 344px;
    top: 159px;
    width: 512px;
    height: 683px;
    display: block;
  }
  .sign-text { font-family: "Montserrat", sans-serif; }
  .tagline-light { font-weight: 300; fill: var(--sign-black); }
  .tagline-bold { font-weight: 800; fill: var(--sign-black); }
  .brand-name { font-weight: 900; fill: var(--sign-red); }
  .phone-number { font-weight: 500; fill: var(--sign-yellow); }
  .web-address { font-weight: 500; fill: var(--sign-white); }
  .panel-yellow { fill: var(--sign-yellow); }
  .panel-black { fill: var(--sign-black); }
  .growth-arrow { fill: var(--sign-red); }
</style>
</head>
<body>
  <svg class="yard-sign" viewBox="0 0 896 1195" role="img" aria-label="DRAVEK roofing yard sign: Connecticut's #1 Company, 203-555-0147, dravekllc.com">
    <rect class="panel-yellow" x="0" y="0" width="896" height="1195"/>
    <polygon class="panel-black" points="0,659 638,564 649,609 896,415 896,1195 0,1195"/>
    <polygon class="growth-arrow" points="0,659 593,420 581,374 896,415 649,609 638,564"/>

    <g class="sign-text" transform="rotate(-13.8 55 339)">
      <text class="tagline-light" x="55" y="339" font-size="108" textLength="712" lengthAdjust="spacingAndGlyphs">Connecticut’s</text>
    </g>
    <g class="sign-text" transform="rotate(-13.8 60 455)">
      <text class="tagline-bold" x="60" y="455" font-size="118" textLength="790" lengthAdjust="spacingAndGlyphs">#1 COMPANY</text>
    </g>

    <text class="sign-text brand-name" x="56" y="875" font-size="246" textLength="782" lengthAdjust="spacingAndGlyphs">DRAVEK</text>
    <text class="sign-text phone-number" x="56" y="993" font-size="106" textLength="784" lengthAdjust="spacingAndGlyphs">203-555-0147</text>
    <text class="sign-text web-address" x="188" y="1072" font-size="66" textLength="512" lengthAdjust="spacing">dravekllc.com</text>
  </svg>
</body>
</html>
```